christmas poster

Gift Vouchers Promotion

Buy 3 of Any Value
Get 1 More Free

The Poster Should be very modern but with a relevance to Christmas

Target Market(s)

Affluent Clients

Font styles to use
Decorative

Colors
ec1f27

Requirements
Must have
• Modern Clean Feel but Relevant to Christmas
Nice to have
• The Offer:
• Buy 3 Gift Vouchers and Receive 1 More Fee
• MUST be Big and Bold
• Include Logo

```html
<!DOCTYPE html>
<html lang="en">
<head>
<meta charset="utf-8">
<title>Buy 3 Gift Vouchers Get 1 Free – Velora Salon &amp; Spa</title>
<link href="https://fonts.googleapis.com/css2?family=Cinzel+Decorative:wght@700&family=Cinzel:wght@700&display=swap" rel="stylesheet">
<style>
  :root {
    --festive-red: #ec1f27;
    --deep-red: #7a0a10;
    --night-red: #3a0407;
    --glow-pink: #f7a0a6;
    --snow: #ffffff;
    --brand-red: #c4161c;
  }
  html, body {
    margin: 0;
    padding: 0;
    width: 800px;
    height: 1200px;
    overflow: hidden;
    background: var(--night-red);
  }
  .poster {
    position: relative;
    width: 800px;
    height: 1200px;
    overflow: hidden;
    background:
      radial-gradient(ellipse 420px 520px at 520px 700px, rgba(247,160,166,0.55), transparent 70%),
      radial-gradient(ellipse 520px 700px at 120px 650px, rgba(255,40,50,0.9), transparent 75%),
      radial-gradient(ellipse 900px 1100px at 400px 700px, var(--festive-red), var(--deep-red) 70%, var(--night-red) 100%);
  }
  .snowfall {
    position: absolute;
    inset: 0;
    width: 800px;
    height: 1200px;
  }
  .offer-line {
    position: absolute;
    left: 0;
    width: 800px;
    margin: 0;
    text-align: center;
    color: var(--snow);
    line-height: 1;
    white-space: nowrap;
    text-shadow: 0 0 18px rgba(255,255,255,0.35), 0 3px 6px rgba(90,0,0,0.35);
    transform-origin: center top;
  }
  .offer-line--hero {
    font-family: "Cinzel Decorative", "Cinzel", serif;
    font-weight: 700;
    font-size: 190px;
    letter-spacing: 4px;
    transform: scaleY(1.22);
  }
  .offer-line--sub {
    font-family: "Cinzel", serif;
    font-weight: 700;
    font-size: 82px;
    letter-spacing: -1px;
    transform: scaleY(1.05);
  }
  .offer-buy  { top: 128px; }
  .offer-gift { top: 392px; }
  .offer-get  { top: 510px; }
  .offer-free { top: 712px; }

  .brand-glow {
    position: absolute;
    left: 170px;
    top: 975px;
    width: 470px;
    height: 200px;
    background: radial-gradient(ellipse at center, rgba(255,255,255,0.85) 35%, rgba(255,255,255,0.25) 65%, transparent 80%);
  }
  .brand-card {
    position: absolute;
    left: 222px;
    top: 1018px;
    width: 364px;
    height: 102px;
    background: var(--snow);
    display: flex;
    align-items: center;
    justify-content: center;
    gap: 12px;
  }
  .brand-dot {
    width: 14px;
    height: 14px;
    border-radius: 50%;
    background: var(--brand-red);
  }
  .brand-name {
    font-family: "Cinzel", serif;
    font-weight: 700;
    font-size: 36px;
    color: var(--brand-red);
    letter-spacing: 0;
    white-space: nowrap;
  }
</style>
</head>
<body>
  <main class="poster">
    <svg class="snowfall" viewBox="0 0 800 1200" aria-hidden="true">
      <g fill="#ffffff" opacity="0.55">
        <circle cx="40" cy="60" r="3"/><circle cx="150" cy="30" r="2"/><circle cx="260" cy="90" r="3"/>
        <circle cx="390" cy="40" r="2"/><circle cx="520" cy="80" r="3"/><circle cx="640" cy="25" r="2"/>
        <circle cx="760" cy="95" r="3"/><circle cx="30" cy="420" r="3"/><circle cx="770" cy="470" r="3"/>
        <circle cx="60" cy="980" r="4"/><circle cx="140" cy="1060" r="3"/><circle cx="700" cy="990" r="4"/>
        <circle cx="740" cy="1120" r="3"/><circle cx="90" cy="1160" r="3"/><circle cx="640" cy="1170" r="3"/>
        <circle cx="20" cy="760" r="2"/><circle cx="785" cy="700" r="2"/><circle cx="430" cy="960" r="3"/>
        <circle cx="330" cy="990" r="2"/><circle cx="560" cy="950" r="3"/><circle cx="200" cy="940" r="2"/>
      </g>
      <g fill="#ffffff">
        <path d="M105 520 l3 -22 l3 22 l22 3 l-22 3 l-3 22 l-3 -22 l-22 -3z"/>
        <path d="M705 520 l3 -20 l3 20 l20 3 l-20 3 l-3 20 l-3 -20 l-20 -3z"/>
        <path d="M760 745 l3 -22 l3 22 l22 3 l-22 3 l-3 22 l-3 -22 l-22 -3z"/>
        <path d="M310 720 l2 -14 l2 14 l14 2 l-14 2 l-2 14 l-2 -14 l-14 -2z"/>
        <path d="M735 900 l3 -18 l3 18 l18 3 l-18 3 l-3 18 l-3 -18 l-18 -3z"/>
        <path d="M95 140 l2 -12 l2 12 l12 2 l-12 2 l-2 12 l-2 -12 l-12 -2z"/>
      </g>
    </svg>

    <h1 class="offer-line offer-line--hero offer-buy">BUY 3</h1>
    <p class="offer-line offer-line--sub offer-gift">GIFT VOUCHERS</p>
    <p class="offer-line offer-line--hero offer-get">GET 1</p>
    <p class="offer-line offer-line--hero offer-free">FREE!</p>

    <div class="brand-glow"></div>
    <div class="brand-card">
      <span class="brand-dot"></span>
      <span class="brand-name">velora salon &amp; spa</span>
    </div>
  </main>
</body>
</html>
```